Packaging Design Project

I need a box for a hair oil called NEL. 3 color, Simple design .. We are open to new ideas, the over all theme.. Pure and Simple , Natural, Color protect, good for the hair. We started with a basic design and this is the existing website http://nelhaircare.com/

Industry/Entity Type

Hair

```html
<!DOCTYPE html>
<html lang="en">
<head>
<meta charset="utf-8">
<title>NEL Hair Care – Hair Oil Box Front Panel</title>
<link rel="stylesheet" href="https://fonts.googleapis.com/css2?family=PT+Sans:wght@400;700&display=swap">
<style>
  :root {
    --stage: #ffffff;
    --panel-cream: #f8f7e4;
    --leaf-light: #dcebc6;
    --leaf-mid: #b9d89d;
    --brand-red: #9b1c14;
    --label-cream: #fbf9ea;
  }
  * { box-sizing: border-box; margin: 0; padding: 0; }
  html, body {
    width: 771px;
    height: 1200px;
    overflow: hidden;
    background: var(--stage);
    font-family: "PT Sans", sans-serif;
  }
  .canvas {
    position: relative;
    width: 771px;
    height: 1200px;
  }
  .box-front {
    position: absolute;
    left: 170px;
    top: 110px;
    width: 430px;
    height: 980px;
    overflow: hidden;
    box-shadow: 0 0 0 1px #e6e6da;
  }
  .leaf-backdrop {
    position: absolute;
    inset: 0;
    background:
      radial-gradient(ellipse at 30% 70%, var(--leaf-mid) 0%, transparent 55%),
      radial-gradient(ellipse at 85% 25%, var(--leaf-light) 0%, transparent 50%),
      linear-gradient(160deg, var(--panel-cream) 0%, var(--leaf-light) 60%, var(--panel-cream) 100%);
  }
  .brand-label {
    position: absolute;
    left: 38px;
    top: 40px;
    width: 354px;
    height: 190px;
    background: var(--label-cream);
    padding: 12px;
  }
  .brand-frame {
    width: 100%;
    height: 100%;
    border: 1.5px solid var(--brand-red);
    padding: 5px;
  }
  .brand-frame-inner {
    width: 100%;
    height: 100%;
    border: 1.5px dashed var(--brand-red);
    display: flex;
    flex-direction: column;
    align-items: center;
    justify-content: center;
    color: var(--brand-red);
    font-weight: 400;
    letter-spacing: 0.12em;
    text-align: center;
  }
  .brand-name { font-size: 72px; line-height: 1; }
  .brand-line { font-size: 32px; line-height: 1.2; }
  .product-title {
    position: absolute;
    left: 0;
    right: 0;
    top: 262px;
    text-align: center;
    color: var(--brand-red);
    font-size: 24px;
    line-height: 1.25;
    letter-spacing: 0.02em;
    text-transform: uppercase;
  }
  .claims {
    position: absolute;
    left: 0;
    right: 0;
    bottom: 62px;
    text-align: center;
    color: var(--brand-red);
    font-weight: 700;
    font-size: 15px;
    line-height: 1.15;
  }
</style>
</head>
<body>
<main class="canvas">
  <section class="box-front">
    <div class="leaf-backdrop" role="img" aria-label="Pale green pattern of skeleton leaves with fine veins on a cream ground"></div>

    <div class="brand-label">
      <div class="brand-frame">
        <div class="brand-frame-inner">
          <span class="brand-name">NEL</span>
          <span class="brand-line">HAIR CARE</span>
        </div>
      </div>
    </div>

    <h1 class="product-title">Protective hair-oil<br>treatment and<br>styling aid</h1>

    <p class="claims">paraben free · sulfate free · alcohol free<br>alergy testerd</p>
  </section>
</main>
</body>
</html>
```